Outdoor sign for Brightwater Auto Restoration

I need a horizontal 4'x 8' outdoor roadside sign for my classic auto restoration business. I have uploaded colors and our logo. Needs the Brightwater name, a prominent Classic AUTO RESTORATION, phone number and website. We rebuild and restore vintage cars, trucks and 4x4s. I'd like something clean but possibly retro. Classic Auto Restoration is more important than the Brightwater name. It needs to be visible and readable from the street. NO CLIP ART

Target Market(s)

Customers who need their vintage care restored or upgraded. Men and women ages 25-75

Industry/Entity Type

Automotive

Colors
FFC000
F8CF3A
FAE287
FDF2CF
FEFAEE

Requirements
Must have
• Legible. Bright. Readable as a backlit 4' x 8' large horizontal sign (roughly 120cm X 240cm)
Nice to have
• Use of the Brightwater logo/type, Complete or Classic before prominent AUTO RESTORATION
Should not have
• Clip art of old cars or icons. And we don't want the Brightwater Logo from the website because it wont be legible from the road. I have included the Illustrator file for Brightwater text in the uploads

```html
<!DOCTYPE html>
<html lang="en">
<head>
<meta charset="utf-8">
<title>Brightwater Auto Restoration – Roadside Sign</title>
<link href="https://fonts.googleapis.com/css2?family=Lobster&family=Oswald:wght@500;700&display=swap" rel="stylesheet">
<style>
  :root{
    --backdrop:#9ecbf7;
    --cream:#f7f4e1;
    --panel:#1f2a30;
    --panel-light:#2c3a41;
    --amber:#f5a90f;
  }
  *{box-sizing:border-box;margin:0;padding:0}
  html,body{width:800px;height:1200px;overflow:hidden}
  body{background:var(--backdrop);position:relative}

  .sign{
    position:absolute;left:40px;top:420px;width:720px;height:360px;
    background:var(--cream);padding:14px;
    box-shadow:0 4px 8px rgba(0,0,0,.18);
  }
  .sign__panel{
    position:relative;width:100%;height:100%;overflow:hidden;
    background:radial-gradient(ellipse at 50% 55%, var(--panel-light) 0%, var(--panel) 75%);
  }
  .sign__name-tab{
    position:absolute;left:50%;top:0;transform:translateX(-50%);
    background:var(--cream);padding:0 26px 4px;height:40px;
    border-radius:0 0 8px 8px;
    font-family:"Oswald",sans-serif;font-weight:700;font-size:36px;line-height:38px;
    color:var(--amber);letter-spacing:.5px;white-space:nowrap;
  }
  .sign__headline{
    position:absolute;left:0;right:0;top:58px;text-align:center;
    font-family:"Lobster",cursive;font-weight:400;color:var(--cream);line-height:1;
  }
  .sign__headline-line{display:block;font-size:76px}
  .sign__headline-line--second{margin-top:-6px}

  .sign__contact{
    position:absolute;left:57px;top:260px;width:579px;height:52px;
    display:flex;border:2px solid var(--amber);
    font-family:"Oswald",sans-serif;font-weight:500;color:var(--cream);
    font-size:27px;line-height:48px;
  }
  .sign__phone{width:215px;text-align:center;border-right:2px solid var(--amber)}
  .sign__web{flex:1;text-align:center;letter-spacing:.2px}
</style>
</head>
<body>
  <section class="sign" aria-label="Brightwater Auto Restoration roadside sign">
    <div class="sign__panel" role="img" aria-label="Dark sunburst background with sparkle accents">
      <div class="sign__name-tab">BRIGHTWATER</div>
      <h1 class="sign__headline">
        <span class="sign__headline-line">Complete Auto</span>
        <span class="sign__headline-line sign__headline-line--second">Restoration</span>
      </h1>
      <div class="sign__contact">
        <span class="sign__phone">501-555-0142</span>
        <span class="sign__web">BRIGHTWATERAUTOWORKS.COM</span>
      </div>
    </div>
  </section>
</body>
</html>
```